ARC VOLLEY Business Card Project

I'd like to request a business card design for the new company I've launched.
The name of the company is "ARC VOLLEY" an indoor unmanned tennis practice facility.
We would like to see designs that use our brand identity color in the logo I've attached.
We hope to get the design with modern, luxurious and elegant tone and manner.
We hope the logo should not be too big.

Business card must have elements as below:
- Logo (One of the logos I've attached)
- Name (In Korean Text) : 박 서 윤
- Title (In Korean Text) : 대표
- Phone Number : 010-8472-3916
- Email Address : seoyun.park@arcvolley-example.co.kr
- Website : www.arcvolley-example.co.kr
- Instagram : arcvolley
- Address (In Korean text) : 경기도 용인시 수지구 풍덕천로 456 미래타워 5층 501호, 502호

Target Market(s)

Tennis amateurs in 20 to 40s

Industry/Entity Type

Sports, Hobby

Contact Information for Business Card

- Logo (One of the logos I've attached) - Name (In Korean Text) : 박 서 윤 - Title (In Korean Text) : 대표 - Phone Number : 010-8472-3916 - Email Address : seoyun.park@arcvolley-example.co.kr - Website : www.arcvolley-example.co.kr - Instagram : arcvolley - Address (In Korean text) : 경기도 용인시 수지구 풍덕천로 456 미래타워 5층 501호, 502호

Font styles to use
Sans Serif

Requirements
Must have
• Double sided
Nice to have
• Logo with intaglio or relief embossing
Should not have
• Logo should not be too big.

```html
<!DOCTYPE html>
<html lang="ko">
<head>
<meta charset="utf-8">
<title>ARC VOLLEY Business Card</title>
<link rel="stylesheet" href="https://fonts.googleapis.com/css2?family=Noto+Sans+KR:wght@400;500&display=swap">
<style>
  :root {
    --bg: #f1f1f1;
    --green: #2e5339;
    --white: #ffffff;
    --ring-light: #e1e5e1;
    --ring-dark: rgba(255, 255, 255, 0.14);
  }
  * { margin: 0; padding: 0; box-sizing: border-box; }
  html, body { width: 1200px; height: 918px; overflow: hidden; }
  body {
    background: var(--bg);
    font-family: "Noto Sans KR", sans-serif;
    position: relative;
  }
  .card {
    position: absolute;
    top: 300px;
    width: 529px;
    height: 318px;
    overflow: hidden;
  }
  .card--front { left: 60px; background: var(--white); }
  .card--back { left: 611px; background: var(--green); color: var(--white); }

  .deco-ring {
    position: absolute;
    width: 150px;
    height: 150px;
    border-radius: 50%;
  }
  .card--front .deco-ring { left: 443px; top: 171px; border: 9px solid var(--ring-light); }
  .card--back .deco-ring { left: -108px; top: 171px; border: 9px solid var(--ring-dark); }

  .brand {
    position: absolute;
    display: flex;
    align-items: center;
    gap: 10px;
    font-weight: 500;
    letter-spacing: 0.06em;
    white-space: nowrap;
  }
  .brand__dot { border-radius: 50%; flex: none; }
  .card--front .brand {
    left: 50%; top: 159px; transform: translate(-50%, -50%);
    font-size: 30px; color: var(--green);
  }
  .card--front .brand__dot { width: 38px; height: 38px; background: var(--green); }
  .card--back .brand {
    left: 146px; top: 158px; transform: translate(-50%, -50%);
    flex-direction: column; gap: 10px;
    font-size: 17px; color: var(--white);
  }
  .card--back .brand__dot { width: 46px; height: 46px; background: var(--white); }

  .person { position: absolute; left: 274px; top: 44px; }
  .person__name {
    font-size: 24px; font-weight: 400; line-height: 30px;
    letter-spacing: 0.35em;
    width: 112px; border-bottom: 1px solid var(--white);
    white-space: nowrap;
  }
  .person__title { font-size: 14px; line-height: 20px; margin-top: 2px; }

  .contact { position: absolute; left: 274px; top: 152px; list-style: none; }
  .contact__item {
    display: flex; align-items: flex-start; gap: 12px;
    font-size: 11.5px; line-height: 15px; margin-bottom: 10px;
  }
  .contact__icon { width: 18px; height: 18px; flex: none; }
  .contact__text { padding-top: 2px; white-space: nowrap; }
  .contact__item--address .contact__text { white-space: normal; width: 210px; }
</style>
</head>
<body>
  <section class="card card--front">
    <div class="deco-ring" aria-hidden="true"></div>
    <div class="brand"><span class="brand__dot"></span>ARC VOLLEY</div>
  </section>

  <section class="card card--back">
    <div class="deco-ring" aria-hidden="true"></div>
    <div class="brand"><span class="brand__dot"></span>ARC VOLLEY</div>

    <div class="person">
      <p class="person__name">박 서 윤</p>
      <p class="person__title">대표</p>
    </div>

    <ul class="contact">
      <li class="contact__item">
        <svg class="contact__icon" viewBox="0 0 24 24" fill="#fff"><path d="M6.6 10.8a15 15 0 0 0 6.6 6.6l2.2-2.2a1 1 0 0 1 1-.25 11.4 11.4 0 0 0 3.6.57 1 1 0 0 1 1 1V20a1 1 0 0 1-1 1A17 17 0 0 1 3 4a1 1 0 0 1 1-1h3.5a1 1 0 0 1 1 1c0 1.25.2 2.45.57 3.57a1 1 0 0 1-.25 1z"/></svg>
        <span class="contact__text">010-8472-3916</span>
      </li>
      <li class="contact__item">
        <svg class="contact__icon" viewBox="0 0 24 24" fill="#fff"><path d="M2 5h20v14H2z"/><path d="M2 5l10 7 10-7" fill="none" stroke="#2e5339" stroke-width="1.6"/></svg>
        <span class="contact__text">seoyun.park@arcvolley-example.co.kr</span>
      </li>
      <li class="contact__item">
        <svg class="contact__icon" viewBox="0 0 24 24" fill="none" stroke="#fff" stroke-width="1.4"><circle cx="12" cy="12" r="9.5"/><ellipse cx="12" cy="12" rx="4" ry="9.5"/><path d="M2.5 12h19M4 7h16M4 17h16"/></svg>
        <span class="contact__text">www.arcvolley-example.co.kr</span>
      </li>
      <li class="contact__item">
        <svg class="contact__icon" viewBox="0 0 24 24" fill="#fff" aria-label="Instagram"><circle cx="12" cy="12" r="5"/></svg>
        <span class="contact__text">arcvolley</span>
      </li>
      <li class="contact__item contact__item--address">
        <svg class="contact__icon" viewBox="0 0 24 24" fill="#fff"><path d="M12 2a7 7 0 0 0-7 7c0 5 7 13 7 13s7-8 7-13a7 7 0 0 0-7-7zm0 9.5A2.5 2.5 0 1 1 12 6.5a2.5 2.5 0 0 1 0 5z"/></svg>
        <span class="contact__text">경기도 용인시 수지구 풍덕천로 456 미래타워 5층 501호, 502호</span>
      </li>
    </ul>
  </section>
</body>
</html>
```